Website Velmoraq Athletics

Velmoraq Athletics needs an update for our corporate website www.velmoraqathletics.com.
We feel the current website is too cluttered with various bits and pecies and strive to a more simpler, easier to navigate website.
We encourage designers to start with a blank canvas, but few aspects of the current website should remain:
- The four lines of business: Sports Media Services, Sports Content Services, Sports Event Services and Sports Federation Services should have a central place on the new site.
- The colour scheme of our house style (black, white and grey/silver) needs to be honoured.
- Our logo should remain as it is (with background intact). Focus on our preferred company logo, found here: http://www.velmoraqathletics.com/download/logos/JPEG/VA_logo_on_white.jpg
- A place where visitors can view the latest company headlines. Only the headlines will suffice.
- It should be clear that Velmoraq Athletics is a sports company. An inventive way of linking our ability of providing sports data with sports images would highly appreciated.
All other components of the current website can remain or be removed/tweaked as the designer pleases. We are open to a complete new look and feel.
A redesign of the homepage should have your focus, but it would be great if the frame work of the design is usable for the other pages of our website as well.
Velmoraq Athletics keywords that reflect on our company: fast, accurate, innovative, intelligent, no-nonsense, business-aimed, passionate about sports, global, modern.
Target Market(s)
international media (tv stations, newspapers), sports federations, olympic committees, sports results websites, sport app builders
Look and feel

```html
<!DOCTYPE html>
<html lang="en">
<head>
<meta charset="utf-8">
<title>Velmoraq Athletics</title>
<link href="https://fonts.googleapis.com/css2?family=Play:wght@400;700&display=swap" rel="stylesheet">
<style>
:root{
  --black:#050505;
  --frame:#2b2b2b;
  --white:#ffffff;
  --panel:#e4e4e4;
  --line:#d2d2d2;
  --text:#333333;
  --muted:#555555;
  --orange:#f39a1e;
  --silver-dark:#8c8c8c;
  --silver-light:#f4f4f4;
}
*{margin:0;padding:0;box-sizing:border-box}
html,body{width:954px;height:1200px;overflow:hidden;background:var(--frame)}
body{font-family:"Play",sans-serif;color:var(--text);position:relative}
.site{position:absolute;left:20px;top:0;width:914px;height:1200px;background:var(--white)}
.header{position:absolute;left:0;top:0;width:914px;height:272px;background:var(--black);overflow:hidden}
.header-glow{position:absolute;left:0;top:0;width:560px;height:232px;
  background:radial-gradient(ellipse 260px 130px at 300px 110px,#ff7a1a 0%,#c0400c 35%,#3a1004 70%,transparent 100%)}
.header-photo{position:absolute;left:580px;top:0;width:334px;height:232px;
  background:linear-gradient(160deg,#3a3a3a 0%,#151515 55%,#5a0c0c 80%,#1a0505 100%)}
.brand{position:absolute;left:102px;top:36px;font-weight:700;font-size:34px;color:var(--white);letter-spacing:1px}
.brand-rule{position:absolute;left:192px;top:80px;width:380px;height:3px;background:linear-gradient(90deg,#000,#777 60%,#222)}
.nav{position:absolute;left:0;top:236px;width:914px;height:36px}
.nav a{position:absolute;top:8px;color:var(--white);text-decoration:none;font-size:17px}
.services{position:absolute;left:0;top:253px;width:445px;height:278px;background:var(--white);border-radius:0 14px 0 0;padding:14px 14px 0 12px}
.services-inner{background:var(--panel);height:264px;border-radius:4px}
.service{position:relative;height:63px;border-bottom:1px solid #fafafa;padding:10px 0 0 21px}
.service h3{font-weight:400;font-size:19px;color:#2d2d2d}
.service p{font-size:8.5px;color:var(--muted);margin-top:2px}
.service .more{font-size:7px;color:var(--orange)}
.badges{position:absolute;right:18px;top:16px;display:flex;gap:5px}
.badges span{width:41px;height:26px;background:var(--white);border:1px solid #999}
.events{position:absolute;left:448px;top:276px;width:465px;height:255px;background:var(--white);border-radius:14px 14px 0 0;padding:10px 12px 0 12px}
.events-inner{background:var(--panel);height:245px;padding:12px 18px 0 22px;border-radius:6px}
.events h2{font-size:20px;color:var(--orange);font-weight:700}
.event{border-bottom:1px solid #f6f6f6;padding:6px 0 10px}
.event h4{font-weight:400;font-size:11px;margin-bottom:5px}
.event p{font-size:10px;line-height:1.15;color:#444}
.band{position:absolute;left:-6px;top:531px;width:923px;height:49px;
  background:linear-gradient(180deg,#b8b8b8 0%,var(--silver-light) 30%,#d6d6d6 55%,var(--silver-dark) 100%)}
.news-tab{position:absolute;left:8px;top:575px;width:226px;height:72px;background:var(--white);
  border:1px solid #ccc;transform:rotate(-7deg);box-shadow:2px 3px 4px rgba(0,0,0,.25);border-radius:0 0 8px 8px}
.news-tab span{position:absolute;left:22px;top:24px;font-size:25px;font-weight:700;color:var(--orange)}
.rule{position:absolute;left:16px;width:874px;height:1px;background:var(--line)}
.news-item{position:absolute;left:16px;width:874px}
.news-thumb{position:absolute;left:0;width:176px;height:131px;background:linear-gradient(180deg,#cfcfcf,#f2f2f2);border-radius:3px}
.news-thumb .photo{position:absolute;left:20px;top:22px;width:140px;height:90px}
.news-body{position:absolute;left:199px;width:675px}
.news-body h3{font-weight:400;font-size:18px;color:var(--orange);margin-bottom:6px}
.news-body p{font-size:13.5px;line-height:1.14;color:#333;margin-bottom:14px}
.footer{position:absolute;left:0;top:1067px;width:914px;height:133px;background:var(--black);color:#ddd}
.foot-col{position:absolute;top:18px}
.foot-col h5{font-weight:400;font-size:12px;color:#eee;margin-bottom:12px}
.foot-col li{list-style:none;font-size:10px;line-height:15px;color:#ccc}
.copyright{position:absolute;left:22px;top:110px;font-size:8px;color:#bbb}
.enews{position:absolute;left:752px;top:16px;width:132px;height:103px;background:#3a3a3a;border-radius:3px;padding:3px 4px}
.enews h6{font-size:9px;text-align:center;color:#fff}
.enews .field{display:flex;gap:3px;margin:2px 0 3px}
.enews .field span{background:#fff;color:#333;font-size:9px;height:13px;line-height:13px;padding:0 3px}
.enews .social{display:flex;align-items:center;gap:6px;height:15px;border-bottom:1px solid #555;font-size:7px;color:#ddd}
.enews .social i{display:block;width:10px;height:10px;border-radius:2px}
.enews .letter{margin-top:4px;background:#fff;color:#000;font-size:9px;font-weight:700;text-align:center;height:14px;line-height:14px}
</style>
</head>
<body>
<div class="site">
  <header class="header">
    <div class="header-glow"></div>
    <div class="header-photo" role="img" aria-label="Close-up of a dark sports shoe with glowing red sole details"></div>
    <div class="brand">Velmoraq Athletics</div>
    <div class="brand-rule"></div>
    <nav class="nav">
      <a style="left:473px">About us</a>
      <a style="left:599px">Contact</a>
      <a style="left:716px">Jobs</a>
      <a style="left:819px">Web Shop</a>
    </nav>
  </header>

  <section class="services">
    <div class="services-inner">
      <div class="service"><h3>Sports Media Services</h3><p>Ultimate Sports Intelligence for journalists.</p><span class="more">read more</span>
        <div class="badges"><span></span><span></span><span></span></div></div>
      <div class="service"><h3>Sports Content Services</h3><p>Fastest richest reliable sports statistics &amp; news channel</p><span class="more">read more</span>
        <div class="badges"><span></span><span></span><span></span></div></div>
      <div class="service"><h3>Sports Event Services</h3><p>The best media Support an Event organizer can get</p><span class="more">read more</span>
        <div class="badges"><span></span><span></span><span></span></div></div>
      <div class="service"><h3>Sports Federation Services</h3><p>One stop shop media solutions for federations.</p><span class="more">read more</span>
        <div class="badges"><span></span><span></span><span></span></div></div>
    </div>
  </section>

  <section class="events">
    <div class="events-inner">
      <h2>Events we are involved in start in:</h2>
      <div class="event"><h4>Quisque vitae pede.</h4><p>Quisque vitae pede. Nam et augue. Sed a elit. Ut vel massa. Suspendisse nibh pede, ultrices vitae,ultrices nec, mollis non nibh.Quisque vitae pede. Nam et augue. Sed a elit Ut vel massa.</p></div>
      <div class="event"><h4>Quisque vitae pede.</h4><p>Quisque vitae pede. Nam et augue. Sed a elit. Ut vel massa. Suspendisse nibh pede, ultrices vitae,ultrices nec, mollis non nibh.Quisque vitae pede. Nam et augue. Sed a elit Ut vel massa.</p></div>
      <div class="event" style="border:0"><h4>Quisque vitae pede.</h4><p>Quisque vitae pede. Nam et augue. Sed a elit. Ut vel massa. Suspendisse nibh pede, ultrices vitae,ultrices nec, mollis non nibh.Quisque vitae pede. Nam et augue. Sed a elit Ut vel massa.</p></div>
    </div>
  </section>

  <div class="band"></div>
  <div class="news-tab"><span>Last News</span></div>

  <div class="rule" style="top:669px"></div>
  <article class="news-item" style="top:682px">
    <div class="news-thumb" style="top:20px"><div class="photo" role="img" aria-label="Tennis player stretching for a shot on a blue court" style="background:linear-gradient(135deg,#1d3f8a,#3a6bc0 50%,#b87a45)"></div></div>
    <div class="news-body"><h3>Quisque vitae pede.</h3>
      <p>Quisque vitae pede. Nam et augue. Sed a elit. Ut vel massa. Suspendisse nibh pede, ultrices vitae,ultrices nec, mollis non nibh.Quisque vitae pede. Nam et augue. Sed a elit Ut vel massa. Suspendisse nibh pede, ultrices vitae,ultrices nec, mollis non nibh. Quisque vitae pede. Nam et augue. Sed a elit. Ut vel massa. Suspendisse nibh pede, ultrices vitae ultrices nec, mollis non nibh.Quisque vitae pede. Nam et augue. Sed a elit. Ut vel massa. Suspendisse nibh pede, ultrices vitae ultrices nec, mollis non nibh...</p>
      <p>Quisque vitae pede. Nam et augue. Sed a elit. Ut vel massa. Suspendisse nibh pede, ultrices vitae ultrices nec, mollis non nibh... Suspendisse nibh pede, ultrices vitae ultrices nec, mollis non nibh...</p></div>
  </article>
  <div class="rule" style="top:855px"></div>
  <article class="news-item" style="top:875px">
    <div class="news-thumb" style="top:9px"><div class="photo" role="img" aria-label="Tennis player returning a ball on a blue court" style="background:linear-gradient(135deg,#12206a,#2a45b0 55%,#0d1440)"></div></div>
    <div class="news-body"><h3>Quisque vitae pede.</h3>
      <p>Quisque vitae pede. Nam et augue. Sed a elit. Ut vel massa. Suspendisse nibh pede, ultrices vitae,ultrices nec, mollis non nibh.Quisque vitae pede. Nam et augue. Sed a elit Ut vel massa. Suspendisse nibh pede, ultrices vitae,ultrices nec, mollis non nibh. Quisque vitae pede. Nam et augue. Sed a elit. Ut vel massa. Suspendisse nibh pede, ultrices vitae ultrices nec, mollis non nibh.Quisque vitae pede. Nam et augue. Sed a elit. Ut vel massa. Suspendisse nibh pede, ultrices vitae ultrices nec, mollis non nibh...</p>
      <p>Quisque vitae pede. Nam et augue. Sed a elit. Ut vel massa. Suspendisse nibh pede, ultrices vitae ultrices nec, mollis non nibh... Suspendisse nibh pede, ultrices vitae ultrices nec, mollis non nibh...</p></div>
  </article>
  <div class="rule" style="top:1037px"></div>

  <footer class="footer">
    <div class="foot-col" style="left:215px"><h5>Quisque vitae pede</h5><ul><li>Quisque vitae</li><li>Quisque vitae pede</li><li>Quisque vitae</li><li>Quisque vitae pede</li></ul></div>
    <div class="foot-col" style="left:380px"><h5>Quisque vitae pede</h5><ul><li>Quisque vitae</li><li>Quisque vitae pede</li><li>Quisque vitae</li><li>Quisque vitae pede</li></ul></div>
    <div class="foot-col" style="left:555px"><h5>Quisque vitae pede</h5><ul><li>Quisque vitae</li><li>Quisque vitae pede</li><li>Quisque vitae</li><li>Quisque vitae pede</li></ul></div>
    <div class="copyright">Copyright © 2011 All rights reserved.</div>
    <div class="enews">
      <h6>eNews sign up</h6>
      <div class="field"><span style="flex:1">Your email</span><span>Go</span></div>
      <div class="social"><i style="background:#3b5a9a"></i>like us on Friendwall</div>
      <div class="social"><i style="background:#4aa8d8"></i>follow us on Chirpline</div>
      <div class="social"><i style="background:#e8872a"></i>subscribe to rss feed</div>
      <div class="letter">eNews Letter</div>
    </div>
  </footer>
</div>
</body>
</html>
```